Contemporary Elegant Business Card Design for an International Trade Company in the Wine Industry

We need a new business card design for an international trade company in the wine and winemaking industry. The overall feel of the card should be contemporary, upscale, luxurious and elegant. It should communicate confidence and professionalism. The colors should complementary to our logo design (burgundy, gold, and black).
Inspiration: rich velvet tapestry
The card should include the following information:
Business: Corvelle Trading/Shipping, LLC.
Name: Martin R. Obrastow
Title: CEO
Email: marty@corvelletrading.example
Phone: 555-482-1957
www.corvelletrading.example
Reason: We'd like the designers that we requested some additional designs from to still submit designs. Thank you!
Business
Contact Information for Business Card
Title: CEO
Phone: 555-482-1957
www.corvelletrading.example

```html
<!DOCTYPE html>
<html lang="en">
<head>
<meta charset="utf-8">
<title>Corvelle Trading/Shipping – Business Card</title>
<link href="https://fonts.googleapis.com/css2?family=Cinzel:wght@600;700&display=swap" rel="stylesheet">
<style>
  :root {
    --burgundy: #7a1420;
    --gold: #c8911f;
    --gold-light: #f2c955;
    --gold-deep: #b27a12;
    --black: #161616;
    --velvet: #2a2a2a;
    --ivory: #f4f3f1;
    --damask: #dcdad6;
    --ink: #111;
    --stage: #e9e4dc;
  }
  * { box-sizing: border-box; margin: 0; padding: 0; }
  html, body { width: 1200px; height: 800px; overflow: hidden; }
  body {
    background: var(--stage);
    font-family: "Cinzel", "Times New Roman", serif;
    display: flex;
    align-items: center;
    justify-content: center;
    gap: 40px;
  }
  .card {
    position: relative;
    width: 540px;
    height: 309px;
    overflow: hidden;
    box-shadow: 0 6px 18px rgba(0,0,0,.18);
  }

  /* Front card */
  .card--front { background: var(--black); }
  .front__texture {
    position: absolute; inset: 0 0 44% 0;
    background:
      radial-gradient(ellipse 30% 45% at 20% 40%, var(--velvet) 0%, transparent 70%),
      radial-gradient(ellipse 30% 45% at 55% 55%, var(--velvet) 0%, transparent 70%),
      radial-gradient(ellipse 30% 45% at 88% 35%, var(--velvet) 0%, transparent 70%),
      var(--black);
  }
  .front__rule {
    position: absolute; left: 0; right: 0; top: 56%;
    height: 3px; background: var(--burgundy);
  }
  .front__band {
    position: absolute; left: 0; right: 0; top: calc(56% + 3px); bottom: 0;
    background: linear-gradient(100deg, var(--gold-deep) 0%, var(--gold-light) 30%, var(--gold) 55%, var(--gold-light) 78%, var(--gold-deep) 100%);
  }
  .brand {
    position: absolute; left: 220px; top: 50px;
    display: flex; align-items: center; gap: 12px;
  }
  .brand__mark { width: 80px; height: 80px; background: var(--burgundy); }
  .brand__name { color: #fff; font-weight: 700; font-size: 26px; letter-spacing: 1px; }
  .contact {
    position: absolute; left: 30px; top: 186px;
    color: var(--ink); line-height: 1.3;
  }
  .contact__name { font-size: 21px; font-weight: 700; letter-spacing: 1px; margin-bottom: 4px; }
  .contact__lines { padding-left: 40px; }
  .contact__line { font-size: 13px; font-weight: 600; letter-spacing: .5px; }

  /* Back card */
  .card--back { background: var(--ivory); }
  .back__texture {
    position: absolute; inset: 0;
    background:
      radial-gradient(ellipse 22% 35% at 12% 30%, var(--damask) 0%, transparent 70%),
      radial-gradient(ellipse 22% 35% at 88% 30%, var(--damask) 0%, transparent 70%),
      radial-gradient(ellipse 22% 35% at 30% 75%, var(--damask) 0%, transparent 70%),
      radial-gradient(ellipse 22% 35% at 72% 75%, var(--damask) 0%, transparent 70%),
      var(--ivory);
  }
  .back__band {
    position: absolute; left: 0; right: 0; bottom: 22px; height: 16px;
    background: var(--burgundy);
  }
  .back__edge {
    position: absolute; left: 0; right: 0; bottom: 0; height: 22px;
    background: var(--ivory);
  }
  .back__gold {
    position: absolute; left: 0; right: 0; bottom: 0; height: 3px;
    background: var(--gold);
  }
  .title-block {
    position: absolute; left: 0; right: 0; top: 96px;
    text-align: center;
  }
  .title-block__name {
    color: var(--burgundy); font-size: 24px; font-weight: 700; letter-spacing: 1.5px;
  }
  .divider {
    display: flex; align-items: center; justify-content: center;
    gap: 10px; margin-top: 6px;
  }
  .divider__flourish {
    width: 70px; height: 3px; background: var(--burgundy); opacity: .8;
  }
  .title-block__role {
    color: var(--gold); font-size: 18px; font-weight: 700; letter-spacing: 2px;
  }
</style>
</head>
<body>

  <section class="card card--front">
    <div class="front__texture" role="img" aria-label="Dark velvet damask pattern"></div>
    <div class="front__rule"></div>
    <div class="front__band" role="img" aria-label="Hammered gold foil band"></div>
    <div class="brand">
      <div class="brand__mark"></div>
      <span class="brand__name">CORVELLE</span>
    </div>
    <div class="contact">
      <p class="contact__name">Martin R. Obrastow</p>
      <div class="contact__lines">
        <p class="contact__line">555-482-1957</p>
        <p class="contact__line">marty@corvelletrading.example</p>
        <p class="contact__line">corvelletrading.example</p>
      </div>
    </div>
  </section>

  <section class="card card--back">
    <div class="back__texture" role="img" aria-label="Embossed white floral damask pattern"></div>
    <div class="back__band"></div>
    <div class="back__edge"></div>
    <div class="back__gold"></div>
    <div class="title-block">
      <p class="title-block__name">Martin R. Obrastow</p>
      <div class="divider">
        <div class="divider__flourish" role="img" aria-label="Arrow flourish ornament"></div>
        <span class="title-block__role">CEO</span>
        <div class="divider__flourish" role="img" aria-label="Arrow flourish ornament"></div>
      </div>
    </div>
  </section>

</body>
</html>
```